Ferris Contracting LLC Business Card Design

I am looking for a creative and unique business card design. We are a commercial construction general contractor. With the name "FERRIS" Contracting, I am hoping to see some neat designs that correlate with the name.

```html
<!DOCTYPE html>
<html lang="en">
<head>
<meta charset="utf-8">
<title>Ferris Contracting LLC — Business Card</title>
<link href="https://fonts.googleapis.com/css2?family=Lato:wght@400;700&display=swap" rel="stylesheet">
<style>
  :root {
    --stage: #9a9a9a;
    --card-white: #ffffff;
    --card-dark: #1b1b1b;
    --brand-blue: #2a8fd6;
    --brand-blue-deep: #1a6fb8;
    --steel: #b9b9b9;
    --steel-light: #dcdcdc;
    --ink: #1e1e1e;
    --ink-soft: #454545;
    --pattern-dark: #222222;
    --pattern-mid: #2c2c2c;
  }
  * { box-sizing: border-box; margin: 0; padding: 0; }
  html, body {
    width: 1200px; height: 1059px; overflow: hidden;
    background: var(--stage);
    font-family: "Lato", Arial, sans-serif;
  }
  .canvas { position: relative; width: 1200px; height: 1059px; }

  .card { position: absolute; overflow: hidden; }

  /* Front */
  .card-front {
    left: 254px; top: 76px; width: 700px; height: 403px;
    background: var(--card-white);
    border-radius: 24px;
  }
  .brand-mark {
    position: absolute; left: 40px; top: 96px;
    display: flex; align-items: center; gap: 10px;
  }
  .brand-dot {
    width: 24px; height: 24px; border-radius: 50%;
    background: var(--brand-blue);
  }
  .brand-name {
    font-weight: 700; font-size: 24px; letter-spacing: 1px;
    color: var(--brand-blue);
  }
  .holder {
    position: absolute; right: 46px; top: 56px; text-align: right;
  }
  .holder-name {
    font-weight: 700; font-size: 28px; color: var(--brand-blue);
    letter-spacing: 0.2px; line-height: 1.1;
  }
  .holder-role {
    font-size: 18px; color: var(--ink); margin-top: 6px;
  }
  .side-tab {
    position: absolute; right: 0; top: 61px; width: 17px; height: 52px;
    background: linear-gradient(180deg, var(--brand-blue), var(--brand-blue-deep));
  }
  .contact-list {
    position: absolute; left: 38px; top: 268px; list-style: none;
  }
  .contact-item {
    display: flex; align-items: center; height: 31.5px;
    font-size: 19px; color: var(--ink);
  }
  .contact-icon { width: 21px; height: 21px; margin-right: 14px; flex: none; }
  .address {
    position: absolute; right: 40px; top: 299px; text-align: right;
    font-size: 18px; color: var(--ink-soft); line-height: 27px;
    font-style: normal;
  }
  .bottom-band { position: absolute; left: 0; bottom: 0; width: 700px; height: 28px; }

  /* Back */
  .card-back {
    left: 242px; top: 568px; width: 724px; height: 412px;
    background: var(--card-dark);
    border-radius: 26px;
  }
  .back-texture {
    position: absolute; inset: 0;
    background: radial-gradient(ellipse at 70% 50%, var(--pattern-mid), var(--pattern-dark) 70%, var(--card-dark));
  }
  .back-name {
    position: absolute; left: 494px; top: 268px;
    font-weight: 700; font-size: 18px; letter-spacing: 1px;
    color: var(--brand-blue);
  }
</style>
</head>
<body>
<main class="canvas">

  <section class="card card-front" aria-label="Card front">
    <div class="brand-mark">
      <span class="brand-dot"></span>
      <span class="brand-name">FERRIS CONTRACTING</span>
    </div>

    <div class="holder">
      <p class="holder-name">MARCUS HALE</p>
      <p class="holder-role">Managing Director</p>
    </div>
    <div class="side-tab"></div>

    <ul class="contact-list">
      <li class="contact-item">
        <svg class="contact-icon" viewBox="0 0 24 24" aria-hidden="true">
          <path fill="var(--brand-blue)" d="M6.6 10.8a15.1 15.1 0 0 0 6.6 6.6l2.2-2.2a1 1 0 0 1 1-.25 11.4 11.4 0 0 0 3.6.57 1 1 0 0 1 1 1V20a1 1 0 0 1-1 1A17 17 0 0 1 3 4a1 1 0 0 1 1-1h3.5a1 1 0 0 1 1 1c0 1.25.2 2.45.57 3.57a1 1 0 0 1-.25 1z"/>
        </svg>
        044-555 218 730
      </li>
      <li class="contact-item">
        <svg class="contact-icon" viewBox="0 0 24 24" aria-hidden="true">
          <rect x="2" y="5" width="20" height="14" fill="var(--brand-blue)"/>
          <path d="M2 5l10 8 10-8" fill="none" stroke="#fff" stroke-width="1.6"/>
        </svg>
        info@ferrisbuild.com
      </li>
      <li class="contact-item">
        <svg class="contact-icon" viewBox="0 0 24 24" aria-hidden="true">
          <circle cx="12" cy="12" r="10" fill="none" stroke="var(--brand-blue)" stroke-width="2"/>
          <path fill="var(--brand-blue)" d="M7 6c2 0 3 1 3 3s-2 2-2 4-2 1-3 0-2-4 2-7zm7 4c2-1 4 0 4 2s-1 5-3 6-2-2-2-3 0-4 1-5z"/>
        </svg>
        www.ferrisbuild.com
      </li>
    </ul>

    <address class="address">
      87 Foundry Lane, Suite 4<br>
      61830, Northbridge
    </address>

    <svg class="bottom-band" viewBox="0 0 700 28" preserveAspectRatio="none" aria-hidden="true">
      <defs>
        <linearGradient id="steel-fade" x1="0" y1="0" x2="0" y2="1">
          <stop offset="0" stop-color="var(--steel-light)"/>
          <stop offset="1" stop-color="var(--steel)"/>
        </linearGradient>
      </defs>
      <polygon points="337,0 700,0 700,22 370,22" fill="url(#steel-fade)"/>
      <polygon points="0,1 322,1 352,22 0,22" fill="var(--brand-blue)"/>
      <rect x="0" y="22" width="700" height="6" fill="var(--brand-blue-deep)"/>
    </svg>
  </section>

  <section class="card card-back" aria-label="Card back">
    <div class="back-texture" role="img" aria-label="Tone-on-tone repeating brand pattern across the dark card back"></div>
    <span class="back-name">FERRIS</span>
  </section>

</main>
</body>
</html>
```